Business Card Design Project

We need a redesign of our business card.
We are a Consulting Property Developer called The Selwick Group
Updates

Thank you all for submissions. Just waiting on managment to decide.

Thank you,

Dorinda

Industry/Entity Type

Business

Requirements
Must have
• we like having the SG a focus in the back ground or on the side
Selwick is our company colour

the wording - property development
and - premium accommodation

our website www.selwickgroup.com.au

persons name
title

p: 1300 582914 f: 1300 582917 m: 0419358027
PO Box 2817, Brackenvale Qld 4215
e: admin@selwickgroup.com.au

```html
<!DOCTYPE html>
<html lang="en">
<head>
<meta charset="utf-8">
<title>The Selwick Group – Business Card</title>
<link href="https://fonts.googleapis.com/css2?family=Open+Sans:wght@400;600;700&display=swap" rel="stylesheet">
<style>
  :root {
    --backdrop: #b48c2e;
    --card-white: #ffffff;
    --brand-maroon: #8c0a34;
    --brand-maroon-deep: #4d0019;
    --brand-maroon-mid: #93103c;
    --brand-grey: #a9a9ab;
    --text-white: #ffffff;
  }
  * { box-sizing: border-box; margin: 0; padding: 0; }
  html, body { width: 1200px; height: 686px; overflow: hidden; }
  body {
    background: var(--backdrop);
    font-family: "Open Sans", Arial, sans-serif;
    position: relative;
  }
  .card {
    position: absolute;
    width: 492px;
    height: 282px;
    border-radius: 19px;
    overflow: hidden;
    box-shadow: 1px 2px 3px rgba(60, 40, 0, 0.45);
  }
  .card--front { left: 93px; top: 131px; background: var(--card-white); }
  .card--back {
    left: 622px; top: 287px;
    background: radial-gradient(ellipse 62% 80% at 50% 45%, var(--brand-maroon-mid) 0%, var(--brand-maroon) 45%, var(--brand-maroon-deep) 100%);
  }
  .wordmark {
    position: absolute;
    left: 0; right: 0; top: 62px;
    display: flex; align-items: center; justify-content: center; gap: 10px;
    font-size: 27px; font-weight: 400; color: var(--brand-maroon);
    letter-spacing: -0.3px;
  }
  .wordmark__dot {
    width: 12px; height: 12px; border-radius: 50%;
    background: var(--brand-maroon);
  }
  .holder {
    position: absolute; left: 53px; top: 134px;
    font-size: 15.5px; font-weight: 700; color: var(--brand-maroon);
    white-space: nowrap;
  }
  .holder__sep { color: var(--brand-grey); font-weight: 400; margin: 0 4px 0 6px; font-size: 13px; }
  .holder__title { color: var(--brand-grey); font-weight: 600; font-size: 12.5px; }
  .card__wave { position: absolute; left: 0; top: 0; width: 492px; height: 282px; }
  .contact {
    position: absolute; left: 0; right: 0; top: 210px;
    color: var(--text-white); font-size: 12px; line-height: 18px;
    text-align: center; white-space: nowrap;
  }
  .contact__line { display: flex; justify-content: center; align-items: center; gap: 10px; }
  .contact__item { display: inline-flex; align-items: center; gap: 2px; }
  .contact__icon { width: 10px; height: 10px; fill: var(--text-white); }
  .back-name {
    position: absolute; left: 0; right: 0; top: 122px;
    text-align: center; color: var(--text-white);
    font-size: 28px; font-weight: 400; letter-spacing: 0.2px;
  }
</style>
</head>
<body>
  <section class="card card--front" aria-label="Business card front">
    <svg class="card__wave" viewBox="0 0 492 282" aria-hidden="true">
      <defs>
        <radialGradient id="frontBand" cx="0.62" cy="0.25" r="0.75">
          <stop offset="0" stop-color="#9a0f3e"/>
          <stop offset="0.5" stop-color="#7d0a2e"/>
          <stop offset="1" stop-color="#4d0019"/>
        </radialGradient>
      </defs>
      <path d="M0 172 C40 186 70 196 110 194 C190 190 260 156 340 150 C400 146 450 148 492 152 L492 282 L0 282 Z" fill="url(#frontBand)"/>
      <path d="M0 170 C40 185 70 194 110 192 C190 188 260 152 340 145 C400 141 450 144 492 148" fill="none" stroke="var(--brand-grey)" stroke-width="5"/>
    </svg>

    <div class="wordmark">
      <span class="wordmark__dot"></span>
      <span>The Selwick Group</span>
    </div>

    <p class="holder">persons name<span class="holder__sep">|</span><span class="holder__title">title</span></p>

    <div class="contact">
      <p class="contact__line">PO Box 2817, Brackenvale Qld 4215</p>
      <p class="contact__line">
        <span class="contact__item">
          <svg class="contact__icon" viewBox="0 0 10 10"><path d="M2 0.5 L3.6 2.6 L2.7 3.6 C3.3 5 4.8 6.6 6.3 7.3 L7.3 6.3 L9.5 7.9 L8.3 9.5 C4.5 9.2 0.8 5.5 0.5 1.7 Z"/></svg>1300 582914
        </span>
        <span class="contact__item">
          <svg class="contact__icon" viewBox="0 0 10 10"><path d="M2.5 0 H7.5 V10 H2.5 Z M3.3 1 V7.5 H6.7 V1 Z"/></svg>0419358027
        </span>
        <span class="contact__item">
          <svg class="contact__icon" viewBox="0 0 10 10"><path d="M2.5 0 H7.5 V3 H2.5 Z M0.5 3.5 H9.5 V8 H0.5 Z M2.5 7 H7.5 V10 H2.5 Z" /></svg>1300 582917
        </span>
      </p>
      <p class="contact__line">
        <span class="contact__item">
          <svg class="contact__icon" viewBox="0 0 10 10"><path d="M0.5 2 H9.5 V8.5 H0.5 Z" /><path d="M0.8 2.3 L5 5.6 L9.2 2.3" fill="none" stroke="#6a0725" stroke-width="0.9"/></svg>admin@selwickgroup.com.au
        </span>
        <span class="contact__item">
          <svg class="contact__icon" viewBox="0 0 10 10"><circle cx="5" cy="5" r="4.4" fill="none" stroke="#fff" stroke-width="1"/><ellipse cx="5" cy="5" rx="1.9" ry="4.4" fill="none" stroke="#fff" stroke-width="0.9"/><path d="M0.6 5 H9.4" stroke="#fff" stroke-width="0.9"/></svg>www.selwickgroup.com.au
        </span>
      </p>
    </div>
  </section>

  <section class="card card--back" aria-label="Business card back">
    <p class="back-name">The Selwick Group</p>
  </section>
</body>
</html>
```